Web Page Design for a Website that Provides Tutoring

I am looking to create an online tutoring website. The website will allow parents or students to contact tutors with a view to instructing them to tutor themselves or their children.

The name of the website is LendYourLessons.

This brief is to create the design for one of the web pages for this web site. I am hoping the same designer will be available to design other pages.

The page I want designed is one of the more complex and I have attached the design as an excel spreadsheet. The web page needs to include all the items on this page but if you want to change the positioning of the items then Im fine with that.

I recently had two logos created for this website. My favourite is the one with a mortar board but im not sure I like the colours. I have attached both of these logos and you can use either of them, change the colours or create something different. I just want a design pleasing to the eye. If the logo is changed I would like that in a seperate file.

So can you please submit designs for this page. I have attached the two logos which you can use, change or if you feel you have a better idea then you can use that.

On the spreadsheet the Send Message, Favourite etc are buttons.

Target Market(s)

People who want to better themselves.
Possible middle class to upper class.

Industry/Entity Type

Tutoring

Number of Pages Required

1 page

Requirements
Must have
• The designs must have alot of the information attached in the spreadsheet.

```html
<!DOCTYPE html>
<html lang="en">
<head>
<meta charset="utf-8">
<title>LendYourLessons – Tutor Profile</title>
<link rel="stylesheet" href="https://fonts.googleapis.com/css2?family=Lato:wght@400;700;900&family=Arimo:wght@400;700&display=swap">
<style>
:root{
  --green:#62a862;
  --green-text:#5aa55a;
  --orange:#f7941d;
  --red:#e74c3c;
  --blue:#4a90d9;
  --ink:#2b2b2b;
  --body:#555;
  --muted:#888;
  --line:#dcdcdc;
  --page:#f1f1f1;
  --card:#fff;
  --footer-a:#9a5a3a;
  --footer-b:#6e3326;
}
*{box-sizing:border-box;margin:0;padding:0}
html,body{width:957px;height:1200px;overflow:hidden;background:var(--page)}
body{font-family:"Arimo",Arial,sans-serif;color:var(--body);position:relative}
.abs{position:absolute}
.header{left:0;top:0;width:957px;height:96px;background:var(--green)}
.brand-box{left:137px;top:0;width:216px;height:96px;background:#fff;display:flex;align-items:center;justify-content:center}
.brand{font-family:"Lato",sans-serif;font-weight:700;font-size:21px;color:var(--orange)}
.contact-line{top:17px;font-size:8px;color:#e8f3e8;display:flex;align-items:center;gap:5px}
.header-rule{left:371px;top:40px;width:440px;height:1px;background:rgba(255,255,255,.3)}
.login{left:749px;top:13px;width:62px;height:17px;border-radius:9px;background:#fff;color:#222;font-size:8px;display:flex;align-items:center;justify-content:center;font-family:"Lato",sans-serif}
.nav{top:63px;left:380px;display:flex;font-family:"Lato",sans-serif;font-weight:700;font-size:8.5px;color:#fff;letter-spacing:.3px}
.nav a{color:#fff;text-decoration:none;position:relative}
.nav a.active::after{content:"";position:absolute;left:0;right:0;top:14px;height:2px;background:#fff}
.card{background:var(--card);box-shadow:0 1px 2px rgba(0,0,0,.06)}
.card-title{font-family:"Lato",sans-serif;font-weight:700;font-size:14px;color:var(--ink)}
.win-ctrl{display:flex;gap:1px}
.win-ctrl span{width:8px;height:7px;border:1px solid #999;display:block}
.msg-input{left:159px;top:112px;width:346px;height:27px;border:1px solid var(--line);font-size:9.5px;color:#777;padding:0 11px;display:flex;align-items:center}
.send{left:510px;top:112px;width:54px;height:27px;background:var(--orange);color:#fff;font-weight:700;font-size:9.5px;display:flex;align-items:center;justify-content:center;font-family:"Lato",sans-serif}
table{border-collapse:collapse;table-layout:fixed}
td,th{border:1px solid var(--line);font-weight:400}
.subjects th{font-size:8px;color:#555;text-align:right;padding:0 6px;height:33px;vertical-align:middle;line-height:1.3}
.subjects td{height:33px;text-align:right;padding:0 6px;font-family:"Lato",sans-serif;font-size:10px;color:var(--green-text)}
.subjects td.dash{color:#888}
.subjects td.subj{text-align:left;color:var(--ink);font-weight:700;font-size:8px}
.avail th{font-size:8px;color:#555;text-align:right;padding:0 7px;height:25px}
.avail td{height:21.6px;text-align:center}
.avail td.slot{text-align:left;padding-left:9px;font-weight:700;font-size:7.5px;color:var(--ink);font-family:"Lato",sans-serif}
.avail svg{width:8px;height:8px;display:block;margin:0 auto}
.legend{left:159px;top:601px;display:flex;font-size:8.5px;color:#555;align-items:center}
.legend span{display:flex;align-items:center;gap:8px}
.legend svg{width:8px;height:8px}
.info-row{left:626px;width:168px;height:28px;border:1px solid #e4e4e4;display:flex;align-items:center;justify-content:space-between;padding:0 8px;font-family:"Lato",sans-serif}
.info-row b{font-size:8px;color:var(--ink)}
.info-row i{font-style:normal;font-size:9.5px;color:var(--green-text)}
.pager{left:731px;top:96px;width:87px;height:28px;background:#888;color:#fff;font-size:10px;display:flex;align-items:center;justify-content:center;gap:8px;font-family:"Lato",sans-serif}
.pager em{width:1px;height:10px;background:#bbb}
.btn{color:#fff;font-family:"Lato",sans-serif;font-weight:900;font-size:10px;letter-spacing:.4px;display:flex;align-items:center;justify-content:center}
.label{font-family:"Lato",sans-serif;font-size:8px;color:#999;letter-spacing:.2px}
.field{border:1px solid #e0e0e0;height:28px;padding:0 8px;display:flex;align-items:center}
.box{width:13px;height:16px;border:1px solid #e0e0e0;display:inline-block}
.boxes{display:flex;align-items:center;gap:2px;font-size:8px;color:#999}
.review{left:212px;width:585px;font-size:8.2px;line-height:10.6px;color:#444}
.review .by{margin-top:9px;color:#666;font-size:7.8px}
.stars{color:#f5b400;font-size:7px;letter-spacing:-.5px;margin-bottom:4px}
.avatar{width:26px;height:26px;border-radius:50%;background:#a79479;color:#fff;font-family:"Lato",sans-serif;font-size:14px;display:flex;align-items:center;justify-content:center}
.footer{left:0;top:1003px;width:957px;height:197px;background:linear-gradient(120deg,var(--footer-a),var(--footer-b))}
.footer-brand{left:0;top:1070px;width:957px;text-align:center;font-family:"Lato",sans-serif;font-weight:700;font-size:21px;color:#fff}
.footer-rule{left:370px;top:1131px;width:219px;height:1px;background:rgba(255,255,255,.2)}
.copy{left:143px;top:1167px;font-size:8px;color:#fff}
.social{left:460px;top:1165px;display:flex;gap:6px}
.social span{width:7px;height:8px;background:#fff;display:block}
.fnav{left:544px;top:1166px;display:flex;gap:15px;font-family:"Lato",sans-serif;font-weight:700;font-size:8.3px;color:#fff}
.to-top{left:840px;top:1152px;width:26px;height:26px;border:1px solid #fff;border-radius:50%;display:flex;align-items:center;justify-content:center}
</style>
</head>
<body>
<svg width="0" height="0" style="position:absolute">
  <symbol id="ok" viewBox="0 0 10 10"><circle cx="5" cy="5" r="5" fill="#5cb85c"/><path d="M2.8 5.1l1.5 1.5 3-3" stroke="#fff" stroke-width="1.3" fill="none"/></symbol>
  <symbol id="taken" viewBox="0 0 10 10"><circle cx="5" cy="5" r="5" fill="#e74c3c"/><path d="M3.3 3.3l3.4 3.4M6.7 3.3l-3.4 3.4" stroke="#fff" stroke-width="1.3"/></symbol>
  <symbol id="reserved" viewBox="0 0 10 10"><circle cx="5" cy="5" r="5" fill="#f7941d"/><path d="M2.8 5h4.4" stroke="#fff" stroke-width="1.4"/></symbol>
  <symbol id="no" viewBox="0 0 10 10"><path d="M0 5h10" stroke="#4a90d9" stroke-width="1.6"/></symbol>
</svg>

<header>
  <div class="abs header"></div>
  <div class="abs brand-box"><span class="brand">LendYourLessons</span></div>
  <div class="abs contact-line" style="left:381px">
    <svg width="7" height="7" viewBox="0 0 10 10"><path d="M2 1l2 2-1 1.5c.8 1.5 1.8 2.5 3.5 3.5L8 6l2 2-1.5 1.8C4.5 9.5.5 5.5.2 2.5z" fill="#fff"/></svg>+00 000 000 0000</div>
  <div class="abs contact-line" style="left:487px">
    <svg width="8" height="6" viewBox="0 0 12 9"><rect width="12" height="9" fill="#fff"/><path d="M0 0l6 5 6-5" stroke="#62a862" fill="none"/></svg>&nbsp;info@lendyourlessons.com</div>
  <div class="abs login">LOG IN</div>
  <div class="abs header-rule"></div>
  <nav class="abs nav">
    <a style="margin-right:32px">HOME</a><a class="active" style="margin-right:32px">SEARCH</a><a style="margin-right:32px">STUDENT</a><a style="margin-right:34px">TUTOR</a><a style="margin-right:34px">ABOUT</a><a>CONTACT</a>
  </nav>
</header>

<main>
  <!-- message card -->
  <section class="abs card" style="left:138px;top:96px;width:449px;height:70px"></section>
  <div class="abs msg-input">Write here...</div>
  <div class="abs send">SEND</div>

  <!-- subjects -->
  <section class="abs card" style="left:138px;top:184px;width:449px;height:187px"></section>
  <h2 class="abs card-title" style="left:159px;top:205px">SUBJECTS TAUGHT</h2>
  <div class="abs win-ctrl" style="left:546px;top:212px"><span></span><span></span></div>
  <table class="abs subjects" style="left:159px;top:245px;width:405px">
    <colgroup><col style="width:78px"><col style="width:55px"><col style="width:54px"><col style="width:54px"><col style="width:53px"><col style="width:53px"><col style="width:58px"></colgroup>
    <tr><th></th><th>Primary</th><th>Secondary</th><th>GCSE</th><th>A-Level</th><th>University</th><th>Adult<br>Learner</th></tr>
    <tr><td class="subj">BIOLOGY</td><td>£20</td><td class="dash">–</td><td>£25</td><td>£30</td><td class="dash">–</td><td class="dash">–</td></tr>
    <tr><td class="subj">CHEMISTRY</td><td>£20</td><td class="dash">–</td><td>£25</td><td>£30</td><td class="dash">–</td><td class="dash">–</td></tr>
  </table>

  <!-- availability -->
  <section class="abs card" style="left:138px;top:390px;width:449px;height:246px"></section>
  <h2 class="abs card-title" style="left:159px;top:412px">AVAILABILITY</h2>
  <div class="abs win-ctrl" style="left:546px;top:419px"><span></span><span></span></div>
  <table class="abs avail" style="left:159px;top:452px;width:405px">
    <colgroup><col style="width:54px"><col style="width:50px"><col style="width:51px"><col style="width:50px"><col style="width:50px"><col style="width:51px"><col style="width:49px"><col style="width:50px"></colgroup>
    <tr><th></th><th>Mon</th><th>Tue</th><th>Wed</th><th>Thu</th><th>Fri</th><th>Sat</th><th>Sun</th></tr>
    <tr><td class="slot">7-8 AM</td><td><svg><use href="#ok"/></svg></td><td><svg><use href="#ok"/></svg></td><td><svg><use href="#ok"/></svg></td><td><svg><use href="#ok"/></svg></td><td><svg><use href="#ok"/></svg></td><td><svg><use href="#ok"/></svg></td><td><svg><use href="#ok"/></svg></td></tr>
    <tr><td class="slot">8-9 AM</td><td><svg><use href="#ok"/></svg></td><td><svg><use href="#ok"/></svg></td><td><svg><use href="#ok"/></svg></td><td><svg><use href="#taken"/></svg></td><td><svg><use href="#ok"/></svg></td><td><svg><use href="#taken"/></svg></td><td><svg><use href="#ok"/></svg></td></tr>
    <tr><td class="slot">4-5 PM</td><td><svg><use href="#ok"/></svg></td><td><svg><use href="#taken"/></svg></td><td><svg><use href="#ok"/></svg></td><td><svg><use href="#ok"/></svg></td><td><svg><use href="#ok"/></svg></td><td><svg><use href="#ok"/></svg></td><td><svg style="width:13px;margin-top:-3px"><use href="#no"/></svg></td></tr>
    <tr><td class="slot">5-6 PM</td><td><svg><use href="#ok"/></svg></td><td><svg><use href="#ok"/></svg></td><td><svg><use href="#ok"/></svg></td><td><svg><use href="#ok"/></svg></td><td><svg><use href="#taken"/></svg></td><td><svg><use href="#reserved"/></svg></td><td><svg><use href="#ok"/></svg></td></tr>
    <tr><td class="slot">7-8 PM</td><td><svg><use href="#ok"/></svg></td><td><svg><use href="#ok"/></svg></td><td><svg><use href="#ok"/></svg></td><td><svg><use href="#ok"/></svg></td><td><svg><use href="#ok"/></svg></td><td><svg><use href="#ok"/></svg></td><td><svg><use href="#ok"/></svg></td></tr>
  </table>
  <div class="abs legend">
    <span style="width:81px"><svg><use href="#ok"/></svg>Available</span>
    <span style="width:75px"><svg><use href="#taken"/></svg>Taken</span>
    <span style="width:86px"><svg><use href="#reserved"/></svg>Reserved</span>
    <span><svg style="width:13px"><use href="#no"/></svg>&nbsp;No</span>
  </div>

  <!-- profile details -->
  <section class="abs card" style="left:604px;top:96px;width:214px;height:290px"></section>
  <div class="abs" style="left:626px;top:96px;width:168px;height:5px;border:1px solid #e4e4e4;border-top:0"></div>
  <div class="abs info-row" style="top:114px"><b>WILLING TO TRAVEL</b><i>Home Only</i></div>
  <div class="abs info-row" style="top:154px"><b>AGE</b><i>24</i></div>
  <div class="abs info-row" style="top:193px"><b>DBS (CRB)</b><i>Verified</i></div>
  <div class="abs info-row" style="top:234px"><b>MEMBER SINCE</b><i>11 months ago</i></div>
  <div class="abs info-row" style="top:273px"><b>LAST LOGGED IN</b><i>2 days ago</i></div>
  <div class="abs pager">Prev<em></em>Next</div>
  <div class="abs btn" style="left:626px;top:321px;width:168px;height:35px;background:var(--orange)">LEAVE FEEDBACK</div>

  <!-- start rating -->
  <section class="abs card" style="left:604px;top:405px;width:214px;height:239px"></section>
  <h2 class="abs card-title" style="left:626px;top:427px">START RATING</h2>
  <div class="abs win-ctrl" style="left:776px;top:431px"><span></span><span></span></div>
  <div class="abs field label" style="left:626px;top:467px;width:169px">ENTER TUTEE NAME</div>
  <div class="abs label" style="left:626px;top:508px">ENTER DATE</div>
  <div class="abs label" style="left:736px;top:508px">ENTER TIME</div>
  <div class="abs boxes" style="left:626px;top:523px"><span class="box"></span><span class="box"></span>/<span class="box"></span><span class="box"></span>/<span class="box"></span><span class="box"></span></div>
  <div class="abs boxes" style="left:735px;top:523px"><span class="box"></span><span class="box"></span>:<span class="box"></span><span class="box"></span></div>
  <div class="abs label" style="left:626px;top:556px">START RATING</div>
  <div class="abs" style="left:716px;top:552px;color:#c8c8c8;font-size:16px;letter-spacing:-1px">★★★★★</div>
  <div class="abs btn" style="left:626px;top:582px;width:168px;height:35px;background:var(--green)">SUBMIT</div>

  <!-- reviews -->
  <section class="abs card" style="left:138px;top:668px;width:680px;height:285px"></section>
  <h2 class="abs card-title" style="left:159px;top:696px">HARRY’S REVIEWS</h2>
  <div class="abs win-ctrl" style="left:776px;top:700px"><span></span><span></span></div>
  <p class="abs" style="left:159px;top:727px;font-size:9.5px;color:#555">Tutors Name has <span style="color:var(--orange)">2</span> reviews with an average review of <span style="color:var(--orange)">4.0</span></p>

  <div class="abs avatar" style="left:169px;top:765px">R</div>
  <div class="abs review" style="top:762px">
    <div class="stars">★★★★★</div>
    Lorem ipsum dolor sit amet, consectetur adipiscing elit, sed do eiusmod tempor incididunt ut labore et dolore magna aliqua. Ut enim ad minim veniam, quis nostrud exercitation ullamco laboris nisi ut aliquip ex ea commodo consequat. Duis aute irure dolor in repreh enderit in voluptate velit esse cillum.
    <div class="by">by Rahul on Dec 03, 2016</div>
  </div>

  <div class="abs avatar" style="left:169px;top:853px">M</div>
  <div class="abs review" style="top:851px">
    <div class="stars">★★★★★</div>
    Lorem ipsum dolor sit amet, consectetur adipiscing elit, sed do eiusmod tempor incididunt ut labore et dolore magna aliqua. Ut enim ad minim veniam, quis nostrud exercitation ullamco laboris nisi ut aliquip ex ea commodo consequat. Duis aute irure dolor in repreh enderit in voluptate velit esse cillum.
    <div class="by">by Martin on May 15, 2016</div>
  </div>
</main>

<footer>
  <div class="abs footer" role="img" aria-label="Background photo of a hand writing with a pen beside a laptop, in warm brown tones"></div>
  <div class="abs footer-brand">LendYourLessons</div>
  <div class="abs footer-rule"></div>
  <div class="abs copy">Copyright © Lend Your Lessons 2016</div>
  <div class="abs social"><span></span><span></span><span></span></div>
  <nav class="abs fnav"><span>HOME</span><span>SEARCH</span><span>STUDENT</span><span>TUTOR</span><span>ABOUT</span><span>CONTACT</span></nav>
  <div class="abs to-top"><svg width="10" height="6" viewBox="0 0 10 6"><path d="M1 5l4-4 4 4" stroke="#fff" stroke-width="1.3" fill="none"/></svg></div>
</footer>
</body>
</html>
```